Attention grabbing 6x9 postcard

We are looking to have an attention grabbing post card that be sent out to homeowners from our roofing company Olum Roofing. the concept is that on the front it will say something like (STOP THE KNOCKING!
Tired of roofers knocking on your door? Contact us because we value your time as much as you value the roof over your head."
Olum Roofing
OlumRoofing.com
877.612.OLUM
info@olumroofing.com

Please feel free to come up with something very creative. Once we pick the final design we will provide the copy.

```html
<!DOCTYPE html>
<html lang="en">
<head>
<meta charset="utf-8">
<title>Olum Roofing Postcard</title>
<link href="https://fonts.googleapis.com/css2?family=Jost:wght@400;500&display=swap" rel="stylesheet">
<style>
  :root {
    --page-bg: #d9dcdf;
    --card-white: #ffffff;
    --ink: #000000;
    --text-dark: #1a1a1a;
    --text-light: #ffffff;
    --line: #333333;
    --roof-dark: #4a4d52;
    --roof-mid: #7d8187;
    --roof-light: #b9bcc0;
    --sky: #9fb3c8;
  }
  * { margin: 0; padding: 0; box-sizing: border-box; }
  html, body {
    width: 1200px; height: 1200px; overflow: hidden;
    background: var(--page-bg);
    font-family: "Jost", "Futura", sans-serif;
  }
  .postcard {
    position: absolute; left: 205px;
    width: 790px; height: 525px;
    background: var(--card-white);
    overflow: hidden;
  }
  .postcard--front { top: 60px; }
  .postcard--back { top: 618px; }
  .postcard__art { position: absolute; inset: 0; width: 790px; height: 525px; }
  .brand-mark {
    position: absolute; transform: translateX(-50%);
    background: var(--text-dark);
  }
  .postcard--front .brand-mark { left: 185px; top: 88px; width: 78px; height: 78px; }
  .postcard--back .brand-mark { left: 318px; top: 96px; width: 56px; height: 56px; }
  .wordmark {
    position: absolute; transform: translateX(-50%);
    color: var(--text-dark); font-weight: 500; letter-spacing: 0.03em;
    white-space: nowrap; line-height: 1;
  }
  .postcard--front .wordmark { left: 185px; top: 208px; font-size: 25px; }
  .postcard--back .wordmark { left: 318px; top: 181px; font-size: 17.5px; }
  .contact { position: absolute; color: var(--text-light); line-height: 1; }
  .contact__name { font-weight: 500; letter-spacing: 0.02em; }
  .contact__line { display: block; }
  .postcard--front .contact { right: 42px; text-align: right; }
  .postcard--front .contact__name { position: absolute; right: 0; top: 312px; font-size: 25px; white-space: nowrap; }
  .postcard--front .contact__line { position: absolute; right: 0; font-size: 24px; white-space: nowrap; }
  .postcard--back .contact { left: 42px; }
  .postcard--back .contact__name { position: absolute; left: 0; top: 355px; font-size: 20px; white-space: nowrap; }
  .postcard--back .contact__line { position: absolute; left: 0; font-size: 18px; white-space: nowrap; }
</style>
</head>
<body>

<section class="postcard postcard--front">
  <svg class="postcard__art" viewBox="0 0 790 525">
    <defs>
      <linearGradient id="gableGrad" x1="0" y1="0" x2="1" y2="1">
        <stop offset="0" stop-color="var(--sky)"/>
        <stop offset="0.45" stop-color="var(--roof-dark)"/>
        <stop offset="1" stop-color="#a89a88"/>
      </linearGradient>
      <linearGradient id="shingleGradFront" x1="0" y1="0" x2="1" y2="1">
        <stop offset="0" stop-color="var(--roof-light)"/>
        <stop offset="1" stop-color="var(--roof-dark)"/>
      </linearGradient>
    </defs>
    <polygon class="photo-gable" role="img" aria-label="Photo of a house gable with dark shingles and siding"
      points="486,0 790,0 790,59 687,246 361,246" fill="url(#gableGrad)"/>
    <polygon class="band-right" points="790,59 790,525 486,525 339,271 361,246 687,246" fill="var(--ink)"/>
    <rect class="band-left" x="0" y="415" width="150" height="110" fill="var(--ink)"/>
    <polygon class="photo-shingles" role="img" aria-label="Close-up photo of grey roof shingles"
      points="119,446 170,313 370,313 426,446 376,580 170,580" fill="url(#shingleGradFront)"/>
  </svg>
  <div class="brand-mark"></div>
  <div class="wordmark">OLUMROOFING.COM</div>
  <div class="contact">
    <span class="contact__name">OLUM ROOFING</span>
    <span class="contact__line" style="top:372px">OlumRoofing.com</span>
    <span class="contact__line" style="top:403px">877.612.OLUM</span>
    <span class="contact__line" style="top:436px">info@olumroofing.com</span>
  </div>
</section>

<section class="postcard postcard--back">
  <svg class="postcard__art" viewBox="0 0 790 525">
    <defs>
      <linearGradient id="shingleGradBack" x1="0" y1="0" x2="1" y2="1">
        <stop offset="0" stop-color="var(--roof-mid)"/>
        <stop offset="1" stop-color="var(--roof-dark)"/>
      </linearGradient>
    </defs>
    <polygon class="photo-shingles" role="img" aria-label="Close-up photo of grey roof shingles"
      points="0,0 166,0 229,133 170,268 0,268" fill="url(#shingleGradBack)"/>
    <polygon class="band-left" points="0,229 295,229 430,458 395,525 0,525" fill="var(--ink)"/>
    <rect class="stamp-box" x="617.5" y="86.5" width="115" height="136" fill="none" stroke="var(--line)" stroke-width="1.5"/>
    <g class="address-lines" stroke="var(--line)" stroke-width="1.5">
      <line x1="454" y1="317" x2="732" y2="317"/>
      <line x1="454" y1="379" x2="732" y2="379"/>
      <line x1="454" y1="440" x2="732" y2="440"/>
    </g>
  </svg>
  <div class="brand-mark"></div>
  <div class="wordmark">OLUMROOFING.COM</div>
  <div class="contact">
    <span class="contact__name">OLUM ROOFING</span>
    <span class="contact__line" style="top:410px">OlumRoofing.com</span>
    <span class="contact__line" style="top:437px">877.612.OLUM</span>
    <span class="contact__line" style="top:463px">info@olumroofing.com</span>
  </div>
</section>

</body>
</html>
```